Trovanta value proposition infographic

• Update to existing “Trovanta Features” wheel infographic (attached) to be more value proposition focused rather than feature focused.
• We want something fresh and new.
• Content messaging to be the 5 value prop points:
1. Intelligent Payment Capture
2. MultiSplit Payouts
3. Ultra Partnerships
4. NextGen Technology Platform
5. Unrivalled Geographical Coverage
• New artwork to appear on Trovanta assets –trovanta-pay.example, business cards, proposal documents etc. – new artwork will need to be scalable.
• Layout is not locked into being a circle, but other design/layout elements of our website/brand should be considered when redesigning this artwork
• Guidelines and brand assets can be found here: https://www.trovanta-pay.example/promotional-guidelines
• Deliverables: Visual file to use in online and offline marketing campaigns. File types: (in CYMK and/or RGB where applicable) .jpg, .png, EPS, PDF
• Tone and image: Functional, engaging, informative, energetic, accessible.
• We want our audience need to understand Trovanta’s total payment expertise focusing on the 5 points of value (listed below in ‘Messages’). They should want to seek more information on the Trovanta value drivers either through continued navigation through our website or contacting our team.

Target Market(s)

Companies searching for recurring payment proviers

Colors
0054AA
0677BA
7BADD7
CADEEF
E8F1F8
F0912C
F2A743
F7CA91
FBE8D2
FDF5EE

Requirements
Should not have
• The same design replacing the old wording with new words.

```html
<!DOCTYPE html>
<html lang="en">
<head>
<meta charset="UTF-8">
<title>Trovanta Value Propositions</title>
<link rel="stylesheet" href="https://fonts.googleapis.com/css2?family=Montserrat:wght@400;600&display=swap">
<style>
  :root {
    --bg-navy: #383a50;
    --accent-orange: #f2832a;
    --accent-orange-light: #f2a743;
    --card-white: #ffffff;
    --text-dark: #1d1d24;
    --icon-shadow: rgba(0, 0, 0, 0.18);
  }
  * { box-sizing: border-box; margin: 0; padding: 0; }
  html, body {
    width: 1200px;
    height: 450px;
    overflow: hidden;
    background: var(--bg-navy);
    font-family: "Montserrat", sans-serif;
  }
  .value-board {
    position: relative;
    width: 1200px;
    height: 450px;
  }
  .value-card {
    position: absolute;
    top: 150px;
    width: 125px;
    height: 157px;
    border-radius: 20px;
    background: var(--accent-orange);
    box-shadow: 2px 3px 6px rgba(0, 0, 0, 0.25);
  }
  .value-card__body {
    position: absolute;
    top: 6px;
    left: 0;
    right: 0;
    bottom: 0;
    border-radius: 20px;
    background: var(--card-white);
    text-align: center;
  }
  .value-card__icon {
    position: absolute;
    top: 16px;
    left: 50%;
    width: 45px;
    height: 45px;
    margin-left: -24px;
    border-radius: 50%;
    background: var(--card-white);
    box-shadow: 2px 2px 5px var(--icon-shadow);
  }
  .value-card__icon-art {
    position: absolute;
    top: 11px;
    left: 11px;
    width: 23px;
    height: 23px;
    border-radius: 5px;
    background: linear-gradient(135deg, var(--accent-orange-light), var(--accent-orange));
  }
  .value-card__title {
    position: absolute;
    top: 80px;
    left: 0;
    right: 0;
    font-size: 15px;
    font-weight: 600;
    color: var(--accent-orange);
    line-height: 1;
  }
  .value-card__subtitle {
    position: absolute;
    top: 101px;
    left: -6px;
    right: -6px;
    font-size: 10px;
    font-weight: 400;
    color: var(--text-dark);
    line-height: 1;
  }
</style>
</head>
<body>
  <main class="value-board">
    <article class="value-card" style="left:148px">
      <div class="value-card__body">
        <div class="value-card__icon"><div class="value-card__icon-art" role="img" aria-label="Payment cards with a security shield illustration"></div></div>
        <h2 class="value-card__title">Intelligent</h2>
        <p class="value-card__subtitle">Payment Capture</p>
      </div>
    </article>
    <article class="value-card" style="left:347px">
      <div class="value-card__body">
        <div class="value-card__icon"><div class="value-card__icon-art" role="img" aria-label="Hand holding a coin with a shield illustration"></div></div>
        <h2 class="value-card__title">MultiSplit</h2>
        <p class="value-card__subtitle">Payouts</p>
      </div>
    </article>
    <article class="value-card" style="left:545px">
      <div class="value-card__body">
        <div class="value-card__icon"><div class="value-card__icon-art" role="img" aria-label="Handshake over a contract illustration"></div></div>
        <h2 class="value-card__title">Ultra</h2>
        <p class="value-card__subtitle">Partnerships</p>
      </div>
    </article>
    <article class="value-card" style="left:744px">
      <div class="value-card__body">
        <div class="value-card__icon"><div class="value-card__icon-art" role="img" aria-label="Light bulb with gears illustration"></div></div>
        <h2 class="value-card__title">NextGen</h2>
        <p class="value-card__subtitle">Technology Platform</p>
      </div>
    </article>
    <article class="value-card" style="left:942px">
      <div class="value-card__body">
        <div class="value-card__icon"><div class="value-card__icon-art" role="img" aria-label="World map with a location marker illustration"></div></div>
        <h2 class="value-card__title">Unrivalled</h2>
        <p class="value-card__subtitle">Geographical Coverage</p>
      </div>
    </article>
  </main>
</body>
</html>
```